Contemporary Vehicle wrap design

Looking for a contemporary design vehicle wrap. This is for a kitchen and bath remodeling company. We have a Brelm K-380 Truck, Brelm Ovaro Cargo Van and a 12’ enclosed trailer. Attached is our logo

Industry/Entity Type

Construction

Colors

Designer to choose colors to be used in the design.

```html
<!DOCTYPE html>
<html lang="en">
<head>
<meta charset="utf-8">
<title>Marlowe Keane Design – Vehicle Wrap Side Panel</title>
<link rel="stylesheet" href="https://fonts.googleapis.com/css2?family=Montserrat:wght@500;600;700&display=swap">
<style>
  :root {
    --wrap-white: #f1f1f1;
    --ink: #141414;
    --stripe-grey: #8c8c8c;
    --band-grey: #6f6f6f;
    --deep: #2a2a2a;
    --photo-dark: #3a3a3a;
    --photo-light: #6a6a6a;
    --page: #ffffff;
  }
  * { margin: 0; padding: 0; box-sizing: border-box; }
  html, body { width: 1200px; height: 1200px; overflow: hidden; background: var(--page); }
  .canvas {
    position: relative; width: 1200px; height: 1200px;
    font-family: "Montserrat", sans-serif;
  }
  .wrap-panel {
    position: absolute; left: 30px; top: 400px; width: 1140px; height: 330px;
    background: var(--wrap-white); overflow: hidden; border-radius: 6px;
  }
  .panel-art { position: absolute; inset: 0; }
  .license {
    position: absolute; left: 110px; top: 64px;
    font-size: 12px; font-weight: 600; color: var(--ink);
  }
  .brand-block { position: absolute; left: 330px; top: 120px; width: 210px; }
  .brand-name {
    display: flex; align-items: center; gap: 10px;
    border: 2px solid var(--ink); padding: 14px 14px;
    font-size: 28px; font-weight: 700; color: var(--ink); letter-spacing: 1px;
  }
  .brand-mark { width: 16px; height: 16px; background: var(--ink); flex: none; }
  .brand-tagline {
    margin-top: 8px; font-size: 17px; font-weight: 600; color: var(--ink);
    letter-spacing: 1px; text-align: center;
  }
  .web-bar {
    position: absolute; left: 310px; top: 260px; width: 300px; height: 28px;
    background: var(--stripe-grey);
    display: flex; align-items: center; padding-left: 18px;
    font-size: 12px; font-weight: 500; color: #fff; letter-spacing: .3px;
  }
  .phone {
    position: absolute; right: 60px; top: 22px;
    font-size: 21px; font-weight: 700; color: #fff; letter-spacing: 2px;
  }
</style>
</head>
<body>
<div class="canvas">
  <section class="wrap-panel" aria-label="Brelm K-380 side wrap">
    <svg class="panel-art" viewBox="0 0 1140 330" width="1140" height="330" aria-hidden="false">
      <defs>
        <linearGradient id="project-photo-tone" x1="0" y1="0" x2="1" y2="1">
          <stop offset="0" stop-color="var(--photo-light)"/>
          <stop offset="1" stop-color="var(--photo-dark)"/>
        </linearGradient>
      </defs>
      <!-- bed-side project photo -->
      <polygon points="800,0 1140,0 1140,330 700,330" fill="url(#project-photo-tone)" role="img" aria-label="Photo of a finished kitchen remodel"/>
      <!-- top dark strip behind phone -->
      <polygon points="820,0 1140,0 1140,34 806,34" fill="var(--deep)"/>
      <!-- diagonal accent bands -->
      <polygon points="640,250 760,0 800,0 680,250" fill="var(--ink)"/>
      <polygon points="700,330 860,0 890,0 730,330" fill="var(--band-grey)"/>
      <polygon points="560,330 720,0 740,0 580,330" fill="var(--stripe-grey)" opacity=".55"/>
      <!-- lower grey rocker stripe -->
      <rect x="0" y="296" width="700" height="10" fill="var(--stripe-grey)"/>
    </svg>
    <div class="license">Lic#318500274</div>
    <div class="brand-block">
      <div class="brand-name"><span class="brand-mark"></span>MK design</div>
      <div class="brand-tagline">KITCHEN + BATH</div>
    </div>
    <div class="web-bar">www.marlowekeanedesign.com</div>
    <div class="phone">833.555.0142</div>
  </section>
</div>
</body>
</html>
```